Vesit cards for web development company

We need a business card design for our company. The company develops online platforms and conducts marketing consulting. Company logo. The cards must fit in with us (a junior start UP), but they must also be professional enough to impress with investors like banks. We wish you a combination of classic and modern design

Target Market(s)

Business partners and IT and marketing customers

Industry/Entity Type

It Company

Contact Information for Business Card

Folgende Information müssen Drauf.
Name, Position, Telefon Nr., Mobile Nr., E-Mail adresse, Optional sind noch Webadresse und HRB Nummer

Colors

Designer to choose colors to be used in the design.

Requirements
Must have
• The cards have to fit into the logo later and have to be dynamic and serious at the same time

```html
<!DOCTYPE html>
<html lang="en">
<head>
<meta charset="utf-8">
<title>Norvale Development — Business Cards</title>
<link href="https://fonts.googleapis.com/css2?family=Mukta:wght@400;500;600&display=swap" rel="stylesheet">
<style>
  :root {
    --brand-blue: #1473bd;
    --ink-black: #0a0a0a;
    --paper-white: #ffffff;
    --soft-grey: #c9ccd0;
    --backdrop: #e9e7e2;
  }
  * { box-sizing: border-box; margin: 0; padding: 0; }
  html, body { width: 1200px; height: 1200px; overflow: hidden; }
  body {
    background: var(--backdrop);
    font-family: "Mukta", "Helvetica Neue", Arial, sans-serif;
    position: relative;
  }
  .card {
    position: absolute;
    left: 150px;
    width: 900px;
    height: 514px;
    overflow: hidden;
    box-shadow: 0 8px 24px rgba(0,0,0,0.18);
  }
  /* Front side */
  .card-front { top: 58px; background: var(--brand-blue); }
  .card-front .base-band {
    position: absolute; left: 0; right: 0; bottom: 0; height: 92px;
    background: var(--ink-black);
  }
  .card-front .wordmark {
    position: absolute; left: 0; right: 0; top: 170px;
    text-align: center; color: var(--paper-white);
    font-weight: 600; font-size: 56px; letter-spacing: 2px; line-height: 1.05;
  }
  .card-front .wordmark small {
    display: block; font-size: 40px; letter-spacing: 3px;
  }
  .card-front .web {
    position: absolute; left: 0; right: 0; bottom: 112px;
    text-align: center; color: var(--paper-white);
    font-weight: 500; font-size: 26px; letter-spacing: 2px;
  }
  /* Back side */
  .card-back { top: 628px; background: var(--ink-black); }
  .card-back .address-band {
    position: absolute; left: 0; top: 330px; width: 520px; height: 110px;
    background: var(--brand-blue);
  }
  .card-back .edge-block {
    position: absolute; right: 0; top: 150px; width: 70px; height: 90px;
    background: var(--brand-blue);
  }
  .company {
    position: absolute; left: 70px; top: 150px;
  }
  .company .wordmark {
    color: var(--brand-blue); font-weight: 600; font-size: 44px;
    letter-spacing: 2px; line-height: 1;
  }
  .company .wordmark small { display: block; font-size: 34px; letter-spacing: 2px; margin-top: 4px; }
  .company .hrb {
    color: var(--paper-white); font-size: 19px; letter-spacing: 6px; margin-top: 10px;
  }
  .person { position: absolute; left: 470px; top: 110px; }
  .person .name {
    color: var(--brand-blue); font-weight: 500; font-size: 42px; line-height: 1; letter-spacing: 1px;
  }
  .person .role { color: var(--paper-white); font-size: 22px; margin-top: 4px; padding-left: 14px; }
  .contacts { list-style: none; position: absolute; left: 520px; top: 230px; }
  .contacts li {
    display: flex; align-items: center; gap: 10px;
    color: var(--paper-white); font-size: 21px; line-height: 32px;
  }
  .contacts li.gap { margin-top: 18px; }
  .icon { width: 20px; height: 20px; flex: none; }
  .address {
    position: absolute; left: 70px; top: 350px; display: flex; gap: 12px;
    color: var(--paper-white); font-size: 24px; line-height: 32px;
  }
  .address .icon { margin-top: 6px; }
</style>
</head>
<body>

<section class="card card-front" aria-label="Business card front">
  <div class="wordmark">NORVALE<small>DEVELOPMENT</small></div>
  <div class="web">www.companyname.com</div>
  <div class="base-band"></div>
</section>

<section class="card card-back" aria-label="Business card back">
  <div class="edge-block"></div>
  <div class="address-band"></div>

  <div class="company">
    <div class="wordmark">NORVALE<small>DEVELOPMENT</small></div>
    <div class="hrb">HRB No. xx-xx-xxxx</div>
  </div>

  <div class="person">
    <div class="name">JOHN DOE</div>
    <div class="role">Director</div>
  </div>

  <ul class="contacts">
    <li>
      <svg class="icon" viewBox="0 0 20 20"><circle cx="10" cy="10" r="10" fill="var(--brand-blue)"/><path d="M6.5 5.5l2 0 1 2.5-1.3 1a6 6 0 0 0 2.8 2.8l1-1.3 2.5 1 0 2a1 1 0 0 1-1 1A8 8 0 0 1 5.5 6.5a1 1 0 0 1 1-1z" fill="#fff"/></svg>
      1-234-567890
    </li>
    <li>
      <svg class="icon" viewBox="0 0 20 20"><circle cx="10" cy="10" r="10" fill="var(--brand-blue)"/><rect x="7" y="4.5" width="6" height="11" rx="1.2" fill="#fff"/><rect x="8" y="6" width="4" height="6.5" fill="var(--brand-blue)"/></svg>
      1-234-5678900
    </li>
    <li class="gap">
      <svg class="icon" viewBox="0 0 20 20"><circle cx="10" cy="10" r="10" fill="var(--brand-blue)"/><circle cx="10" cy="10" r="5.5" fill="none" stroke="#fff" stroke-width="1.2"/><path d="M4.5 10h11M10 4.5c-2.5 3-2.5 8 0 11M10 4.5c2.5 3 2.5 8 0 11" fill="none" stroke="#fff" stroke-width="1"/></svg>
      www.companyname.com
    </li>
    <li>
      <svg class="icon" viewBox="0 0 20 20"><circle cx="10" cy="10" r="10" fill="var(--brand-blue)"/><rect x="5" y="6.5" width="10" height="7" fill="#fff"/><path d="M5 6.5l5 4 5-4" fill="none" stroke="var(--brand-blue)" stroke-width="1"/></svg>
      john@companyname.com
    </li>
  </ul>

  <div class="address">
    <svg class="icon" viewBox="0 0 20 20"><circle cx="10" cy="10" r="10" fill="var(--paper-white)"/><path d="M10 4a4 4 0 0 1 4 4c0 3-4 8-4 8s-4-5-4-8a4 4 0 0 1 4-4z" fill="var(--brand-blue)"/><circle cx="10" cy="8" r="1.5" fill="#fff"/></svg>
    <div>Dummy city<br>Dummy Country Land</div>
  </div>
</section>

</body>
</html>
```